Discreet simple classy for adult entertainment

I would like a matte black business card with gold writing for my business. Keeping it simple. Having my following:

Lana frost
Events. Entertainment. Promotions
0491726580

or alternatively could have what i had on my previous card below but i think i prefer the above as again - discretion.

Maybe a nice gold line thru the card or some other very simple design . Or not open to ideas/ can be doublesided if any good ideas with that.

included pics of my old bus card. not sure weather i want a photo on it or not. if i do it wont be the same pic. i kinda wanted a card that was discreet so if it was in someones wallet they wouldn't neccessarily realise it was from a stripper.

Target Market(s)

men

Industry/Entity Type

Business

Contact Information for Business Card

Lana frost
0491726580

Requirements
Nice to have
• i don't know i am really open to anything. im giving my cards to guys so something they can have in their wallet that is discreet preferably.

```html
<!DOCTYPE html>
<html lang="en">
<head>
<meta charset="utf-8">
<title>Lana Frost – Business Card</title>
<link rel="stylesheet" href="https://fonts.googleapis.com/css2?family=Kalam:wght@400;700&display=swap">
<style>
  :root {
    --page-bg: #ffffff;
    --card-edge: #8a8a8a;
    --card-dark: #262729;
    --card-mid: #3b3c3f;
    --accent: #f9ab2f;
    --ink: #1f1f1f;
  }
  html, body {
    margin: 0;
    padding: 0;
    width: 1200px;
    height: 704px;
    overflow: hidden;
    background: var(--page-bg);
  }
  .card {
    position: absolute;
    left: 0;
    top: 0;
    width: 1196px;
    height: 700px;
    border: 2px solid var(--card-edge);
    border-radius: 52px;
    overflow: hidden;
    background: radial-gradient(ellipse at 48% 52%, var(--card-mid) 0%, var(--card-dark) 70%);
  }
  .accent-band {
    position: absolute;
    left: 0;
    top: 88px;
    width: 100%;
    height: 116px;
    background: var(--accent);
  }
  .stripes {
    position: absolute;
    left: 0;
    top: 0;
  }
  .name {
    position: absolute;
    left: 122px;
    top: 82px;
    margin: 0;
    font-family: "Kalam", cursive;
    font-weight: 700;
    font-size: 86px;
    line-height: 1.3;
    letter-spacing: 2px;
    text-transform: uppercase;
    color: var(--ink);
    transform: skewX(-4deg);
  }
  .phone {
    position: absolute;
    left: 122px;
    top: 224px;
    margin: 0;
    font-family: "Kalam", cursive;
    font-weight: 700;
    font-size: 58px;
    line-height: 1.2;
    color: var(--accent);
    letter-spacing: 1px;
  }
  .services {
    position: absolute;
    left: 122px;
    top: 424px;
    margin: 0;
    padding: 0;
    list-style: none;
    font-family: "Kalam", cursive;
    font-weight: 400;
    font-size: 52px;
    line-height: 74px;
    color: var(--accent);
    text-transform: uppercase;
    letter-spacing: 2px;
  }
</style>
</head>
<body>
  <div class="card">
    <div class="accent-band"></div>
    <svg class="stripes" width="1196" height="700" viewBox="0 0 1196 700" aria-hidden="true">
      <rect x="955" y="79" width="49" height="133" fill="#222325"/>
      <rect x="1022" y="79" width="47" height="133" fill="#222325"/>
      <rect x="1089" y="79" width="47" height="133" fill="#222325"/>
    </svg>
    <h1 class="name">Lana Frost</h1>
    <p class="phone">0491 726 580</p>
    <ul class="services">
      <li>Events</li>
      <li>Entertainment</li>
      <li>Promotions</li>
    </ul>
  </div>
</body>
</html>
```